Postcard design for Intellectual Property Professional Conference

Seeking design for 5.5" by 8.5" postcard mailer about a conference on tax and finance issues for international IP management. Attendees are lawyers and financial executives. Draft language is attached.

Target Market(s)

The project should have the attached picture of Boston with the caption "Courtesy of the Harborline Meeting & Travelers Council"

Industry/Entity Type

Finance

```html
<!DOCTYPE html>
<html lang="en">
<head>
<meta charset="utf-8">
<title>IP Conference Postcard</title>
<link rel="stylesheet" href="https://fonts.googleapis.com/css2?family=Cormorant+Garamond:wght@500;600&family=Cabin:wght@400;500;600&family=PT+Sans+Narrow:wght@400;700&family=Oswald:wght@700&display=swap">
<style>
:root{
  --stage:#000;
  --paper:#ebeae6;
  --navy:#1d2352;
  --blue:#1f4f8c;
  --gold:#e8c63c;
  --band:#d4d4d4;
  --ink:#1a1a1a;
  --white:#fff;
}
*{margin:0;padding:0;box-sizing:border-box}
html,body{width:1200px;height:985px;overflow:hidden;background:var(--stage)}
.canvas{position:relative;width:1200px;height:985px}
.card{position:absolute;top:118px;width:483px;height:747px;overflow:hidden}
.card--front{left:97px;background:radial-gradient(ellipse at 50% 40%,#f1f0ec 0%,var(--paper) 70%,#e2e1dc 100%)}
.card--back{left:618px;background:var(--blue)}
.abs{position:absolute}

/* front */
.early-banner{left:74px;top:56px;width:336px;height:42px;background:var(--blue);border-radius:6px;color:var(--white);
  font:700 21px/42px "PT Sans Narrow",sans-serif;text-align:center;letter-spacing:.2px}
.title{left:0;top:148px;width:483px;text-align:center;color:var(--navy);
  font:600 40px/45.5px "Cormorant Garamond",serif;letter-spacing:-1.5px}
.title-rule{left:77px;top:338px;width:344px;height:1px;background:#3a3a3a}
.date{left:0;top:347px;width:483px;text-align:center;color:var(--navy);font:500 23px/28px "Cormorant Garamond",serif;letter-spacing:-.5px}
.intro{top:402px;font:400 10.6px/15px "Cabin",sans-serif;color:var(--ink)}
.intro--left{left:90px;width:152px}
.intro--right{left:259px;width:136px}
.org-box{left:140px;top:659px;width:203px;height:56px;background:var(--white);display:flex;flex-direction:column;align-items:center;justify-content:center;gap:4px}
.org-name{display:flex;align-items:center;gap:6px;font:600 10.5px/12px "Cabin",sans-serif;color:var(--blue)}
.org-square{width:11px;height:11px;background:var(--blue)}
.org-note{font:400 6px/7px "Cabin",sans-serif;color:#333}

/* back */
.heading{font:500 21px/24px "Cormorant Garamond",serif;color:var(--gold);letter-spacing:-.5px}
.topics-head{left:52px;top:52px}
.topics{left:58px;top:78px;width:232px;list-style:none;font:400 9.8px/12.4px "Cabin",sans-serif;color:var(--white)}
.topics li{position:relative;padding-left:11px;margin-bottom:4px}
.topics li::before{content:"•";position:absolute;left:0;top:0}
.speaker-divider{left:299px;top:78px;height:296px;border-left:1.5px dotted #c9d3e4}
.speakers-head{left:310px;top:52px}
.speakers{left:317px;top:78px;width:118px;list-style:none;font:400 9.8px/12.4px "Cabin",sans-serif;color:var(--white)}
.speakers li{margin-bottom:5.5px}
.reg-band{left:0;top:388px;width:483px;height:148px;background:var(--band)}
.reg-lead{left:52px;top:402px;font:400 9.8px/14px "Cabin",sans-serif;color:var(--ink)}
.reg-now{left:52px;top:418px;font:700 21px/28px "Oswald",sans-serif;color:var(--navy);letter-spacing:.5px}
.reg-venue{left:52px;top:449px;width:160px;font:400 9.8px/16px "Cabin",sans-serif;color:var(--ink)}
.harbor-photo{left:221px;top:388px;width:262px;height:126px;background:linear-gradient(180deg,#b9d3ea 0%,#d9e6f0 38%,#a88a74 55%,#6b6a5e 72%,#4f6660 85%,#7c8f86 100%)}
.photo-credit{left:220px;top:515px;font:400 12.5px/16px "PT Sans Narrow",sans-serif;color:var(--ink)}
.reg-links{left:52px;top:552px;font:400 9.8px/14.5px "Cabin",sans-serif;color:var(--white)}
.back-rule{left:52px;top:588px;width:378px;height:1px;background:#0f2c55}
.back-address,.back-more{top:595px;font:400 9.6px/14.5px "Cabin",sans-serif;color:#d3ddeb}
.back-address{left:52px}
.back-split{left:182px;top:597px;width:1px;height:40px;background:var(--white)}
.back-more{left:190px}
</style>
</head>
<body>
<div class="canvas">

  <section class="card card--front">
    <div class="abs early-banner">Register Early and Save up to $300</div>
    <h1 class="abs title">Increasing Profits<br>&amp; Protecting Intellectual<br>Property in Developing<br>Growth Markets</h1>
    <div class="abs title-rule"></div>
    <p class="abs date">Boston March 24 &amp; 25, 2016</p>
    <p class="abs intro intro--left">You are cordially invited to attend a comprehensive and practical day and a half conference to examine the tax and legal structuring strategies for increasing profits from Intellectual properties while protecting these important assets when doing business in fast growing developing markets. Intellectual property assets include some of the most important assets of most companies: their patents, trade marks, copyrights, brand names and licensing agreements.</p>
    <p class="abs intro intro--right">Senior tax, legal and financial experts will provide a comprehensive analysis of the legal issues, recent tax &amp; regulatory developments, skills and structuring strategies necessary to maximize profits from IP Migrating IP assets to low tax jurisdiction will also be covered along with dealing with issues of piracy, counterfeiting, infringement and other legal challenges to a company's IP.</p>
    <div class="abs org-box">
      <div class="org-name"><span class="org-square"></span>Meridian Markets Council</div>
      <div class="org-note">Programs for cross-border advisers</div>
    </div>
  </section>

  <section class="card card--back">
    <h2 class="abs heading topics-head">Topics to be covered include:</h2>
    <ul class="abs topics">
      <li>Market trends in IP tax &amp; legal structures</li>
      <li>Proposed US Tax changes and regulatory developments outside the US including European and OECD developments affecting IP, patent box, base erosion and profit splitting (BEPS)</li>
      <li>Overview of the IP landscape in key developing growth markets such as China, India, Brazil, Korea, South Africa, Mexico and other developing markets outside the US.</li>
      <li>Legal issues including litigation, arbitration and use of government assistance to protect IP values in key developing markets.</li>
      <li>Monetizing IP assets and rights in regard to divestitures, spin offs, split offs, M&amp;A, transfers of ownership and securitizations in developing growth markets</li>
      <li>Special Tax Planning and Legal Considerations for IP in Particular Sectors such as Biopharmaceutical, International Sports Licensing, High Tech, Consumer Brands, and Manufacuring</li>
      <li>Restructuring and Migration of IP Assets to Tax Advantaged Jurisdictions</li>
    </ul>
    <div class="abs speaker-divider"></div>
    <h2 class="abs heading speakers-head">Speakers:</h2>
    <ul class="abs speakers">
      <li>Corvane Bio (speaker to be announced)</li>
      <li>Keith Ormond and others (Thorne &amp; Maddox)</li>
      <li>Gaspard L. Delorme, (Ashgrove Kellerman)</li>
      <li>Martin Halvers, Pieter Maas, and Noud Verbeek (Ridley Vance)</li>
      <li>Rina Novakis (Hollis Pemberton)</li>
      <li>Jonah Fairbairn (Marlow Brandt)</li>
      <li>Joel Danner (Sutton &amp; Wexley)</li>
      <li>Kara Winslow (Calder)</li>
      <li>Lena Corwin (Fairholm)</li>
      <li>Others to be announced</li>
    </ul>

    <div class="abs reg-band"></div>
    <p class="abs reg-lead">Seating is limited, we invite you to</p>
    <p class="abs reg-now">REGISTER NOW!</p>
    <p class="abs reg-venue">We look forward to seeing you on Thursday, March 24 at the Boston office of Sutton &amp; Wexley, 8 Harbor Exchange Place, Boston, MA 02110</p>
    <div class="abs harbor-photo" role="img" aria-label="Photograph of the Boston harbor waterfront skyline with boats and a lamppost"></div>
    <p class="abs photo-credit">Courtesy of the Harborline Meeting &amp; Travelers Council</p>

    <p class="abs reg-links">Register at: http://www.meridianforum.org/events/ip-conference-register<br>Or email events@meridianmarkets.org or call 555-014-2290</p>
    <div class="abs back-rule"></div>
    <p class="abs back-address">MeridianMarkets.org<br>17 Orchard Bend Rd.<br>Lexington, MA 02420</p>
    <div class="abs back-split"></div>
    <p class="abs back-more">Want more information on MMC or other programs.<br>Send us an email to events@meridianmarkets.org<br>Or send this back with your address</p>

    <div class="abs org-box">
      <div class="org-name"><span class="org-square"></span>Meridian Markets Council</div>
      <div class="org-note">Programs for cross-border advisers</div>
    </div>
  </section>

</div>
</body>
</html>
```